QUICK: Fresh Ideas for New Home Page Design!

Simply improve on our home page design and provide PSD file.

We are Sunward Coverage, a trusted health insurance comparison site to make shopping and enrolling in Carewell easy. We are certified agents for Pacific Shield Exchange, the state's health insurance marketplace (logo attached).

Use flat UI colors.

Looking for a fun design. Reference websites are:
www.plumvista.com
www.hibrindle.com
www.tolmex.com
www.findcanopy.com
www.trymeadowcoverplan.com

Target Market(s)

Individuals ages 18 - 64 shopping for health insurance for themselves and/or their family members. California residents. Don't have health insurance and want it or have it and looking to change.

Industry/Entity Type

Shopping

Font styles to use
Sans Serif

Colors
faed22
33a6d7
33b7a4

Requirements
Must have
• No stock photos. No medical or doctor images or photos. Use images of families. Friendly. Modern fonts and flat UI colors.
Nice to have
• Create a mock-up logo for Sunward Coverage.
Should not have
• No stock looking photos or images

```html
<!DOCTYPE html>
<html lang="en">
<head>
<meta charset="utf-8">
<title>Sunward Coverage – Home</title>
<link href="https://fonts.googleapis.com/css2?family=Lato:wght@400;700&family=Arimo:wght@400;700&display=swap" rel="stylesheet">
<style>
:root{
  --yellow:#faed22;
  --blue:#33a6d7;
  --teal:#33b7a4;
  --ink:#222;
  --carrier-ink:#5d6770;
  --grey-bar:#d9d9d9;
  --footer:#dde3e8;
  --footer-ink:#7a8590;
  --white:#fff;
}
*{margin:0;padding:0;box-sizing:border-box}
html,body{width:1200px;height:900px;overflow:hidden;background:var(--white)}
body{font-family:"Arimo",Arial,sans-serif;color:var(--ink)}
.page{position:absolute;left:439px;top:0;width:322px;height:900px;background:var(--white);overflow:hidden}

.top-bar{position:absolute;left:0;top:0;width:322px;height:12px;background:var(--grey-bar);font-size:4.5px;line-height:12px}
.top-bar .tagline{position:absolute;left:24px;color:var(--teal)}
.top-bar nav{position:absolute;right:0;top:0;display:flex}
.top-bar nav a{color:#444;text-decoration:none;padding:0 9px}
.top-bar nav a.login{background:var(--yellow);color:#333;padding:0 6px}

.hero-photo{position:absolute;left:0;top:12px;width:322px;height:148px;background:linear-gradient(180deg,#6f9a4a 0%,#b9c8b6 45%,#d7d2c9 65%,#8fbf4e 85%,#a6cf55 100%)}

.intro{position:absolute;left:23px;top:175px;width:292px;font-family:"Lato",sans-serif;font-weight:400;font-size:13.2px;line-height:18px;letter-spacing:-.25px;color:#111}
.intro .brand{color:var(--blue)}

.actions{position:absolute;left:0;top:250px;width:322px}
.action{position:absolute;width:80px;text-align:center;font-size:5.5px;font-weight:400;letter-spacing:.1px}
.action svg{display:block;margin:0 auto 5px}

.feature-band{position:absolute;left:0;top:313px;width:322px;height:288px;background:linear-gradient(160deg,#9fcfe3 0%,#c6e2ec 35%,#7fb8d6 60%,#a9d0e2 100%)}
.notch-top{position:absolute;left:154px;top:313px}
.notch-bottom{position:absolute;left:154px;top:601px}
.feature-band .logo{position:absolute;left:10px;top:12px;font-family:"Lato",sans-serif;font-size:12.5px;color:var(--yellow)}
.feature-band nav{position:absolute;right:10px;top:20px;display:flex;gap:7px;font-size:4.3px;color:var(--white)}
.feature-band nav .current{color:var(--yellow)}
.benefit{position:absolute;width:90px;text-align:center;color:var(--white);font-size:5.8px;line-height:7px}
.benefit svg{display:block;margin:0 auto 6px}
.quote-button{position:absolute;left:98px;top:250px;width:128px;height:24px;background:var(--yellow);color:#333;font-size:10px;line-height:24px;text-align:center;letter-spacing:.2px}

.carriers{position:absolute;left:0;top:620px;width:322px}
.carriers h2{position:absolute;left:11px;top:3px;font-weight:400;font-size:7.5px;color:var(--blue);white-space:nowrap}
.carrier-row{position:absolute;left:11px;top:23px;width:300px;display:flex;justify-content:space-between;list-style:none}
.carrier{font-size:7px;font-weight:700;color:var(--carrier-ink);white-space:nowrap}
.dots{position:absolute;display:flex;gap:10px}
.dots span{width:6px;height:6px;border-radius:50%;background:#e3e3e3}
.dots span.on{background:#c4c4c4}

.testimonial{position:absolute;left:0;top:682px;width:322px;height:94px;background:var(--teal)}
.testimonial .avatar{position:absolute;left:27px;top:8px;width:63px;height:63px;border-radius:50%;border:2px solid var(--white);background:radial-gradient(circle at 45% 40%,#f3d4b2 0%,#e0b48c 45%,#d07898 80%)}
.testimonial blockquote{position:absolute;left:99px;top:28px;width:194px;color:var(--white);font-size:5.9px;line-height:7px}
.testimonial blockquote em{font-style:normal;color:var(--yellow);font-size:7px}
.testimonial .dots{left:142px;top:79px}
.testimonial .dots span{background:var(--white)}
.testimonial .dots span.on{background:#c9c9c9}

.site-footer{position:absolute;left:0;top:776px;width:322px;height:124px;background:var(--footer)}
.social{position:absolute;left:138px;top:12px;display:flex;gap:3px}
.social span{width:7px;height:7px;border-radius:50%;background:#7b848c}
.footer-col{position:absolute;top:28px;font-size:3.6px;line-height:6px;color:var(--footer-ink)}
.footer-col h3{font-size:4.3px;font-weight:700;color:#666;border-bottom:.5px solid #b9c1c8;padding-bottom:1px;margin-bottom:2px;width:46px}
.footer-col ul{list-style:none}
.footer-note{position:absolute;left:0;top:114px;width:322px;text-align:center;font-size:3.4px;color:var(--footer-ink)}
</style>
</head>
<body>
<div class="page">

  <header class="top-bar">
    <span class="tagline">A Brightpath Services Inc. Company</span>
    <nav><a>About Us</a><a>Resources</a><a>Contact Us</a><a class="login">Account login</a></nav>
  </header>

  <div class="hero-photo" role="img" aria-label="Three generations of a smiling family lying together on green grass in a sunny park"></div>

  <h1 class="intro">Hi, we are <span class="brand">Sunward Coverage</span>.<br>A trusted health insurance comparison site to make<br>your shopping and enrolling in Carewell easy.</h1>

  <section class="actions">
    <div class="action" style="left:14px">
      <svg width="33" height="33" viewBox="0 0 33 33"><circle cx="16.5" cy="16.5" r="16.5" fill="var(--yellow)"/><path d="M10 23l2-5 9-9 3 3-9 9z" fill="none" stroke="#fff" stroke-width="1.4"/><path d="M9 25h15" stroke="#fff" stroke-width="1"/></svg>
      APPLY NOW
    </div>
    <div class="action" style="left:121px">
      <svg width="33" height="33" viewBox="0 0 33 33"><circle cx="16.5" cy="16.5" r="16.5" fill="var(--blue)"/><rect x="9" y="9" width="15" height="15" fill="none" stroke="#fff" stroke-width="1.3"/><path d="M11.5 13h7M11.5 16h5M11.5 19h4" stroke="#fff" stroke-width="1"/><circle cx="20" cy="19" r="2.6" fill="var(--blue)" stroke="#fff" stroke-width="1.1"/><path d="M22 21l2.5 2.5" stroke="#fff" stroke-width="1.3"/></svg>
      FIND PLANS
    </div>
    <div class="action" style="left:224px">
      <svg width="33" height="33" viewBox="0 0 33 33"><circle cx="16.5" cy="16.5" r="16.5" fill="var(--teal)"/><path d="M10 17a6.5 6.5 0 0 1 11-5l1.5 1.5M23 16a6.5 6.5 0 0 1-11 5l-1.5-1.5" fill="none" stroke="#fff" stroke-width="2"/><path d="M23 10v4h-4M10 23v-4h4" fill="none" stroke="#fff" stroke-width="1.6"/></svg>
      RENEW NOW
    </div>
  </section>

  <section class="feature-band" role="img" aria-label="Two laughing young children, a boy in blue and a blond girl, playing together on white bedding">
    <div class="logo">Sunward Coverage</div>
    <nav><span class="current">HOME</span><span>HEALTH PLANS</span><span>HEALTH BENEFITS</span><span>AFFORDABLE OPTIONS</span><span>EMPLOYERS</span></nav>

    <div class="benefit" style="left:9px;top:82px">
      <svg width="32" height="32" viewBox="0 0 32 32"><circle cx="16" cy="16" r="16" fill="#fff"/><circle cx="14" cy="14" r="5.5" fill="none" stroke="#111" stroke-width="2"/><path d="M18 18l5.5 5.5" stroke="#111" stroke-width="2.6"/></svg>
      We help you get<br>financial assistance
    </div>
    <div class="benefit" style="left:116px;top:82px">
      <svg width="32" height="32" viewBox="0 0 32 32"><circle cx="16" cy="16" r="16" fill="#fff"/><path d="M20 10H10v13h13V13" fill="none" stroke="#111" stroke-width="1.8"/><path d="M14 19l1-3 8-8 2 2-8 8z" fill="#111"/></svg>
      We help you choose<br>the right plan
    </div>
    <div class="benefit" style="left:219px;top:82px">
      <svg width="32" height="32" viewBox="0 0 32 32"><circle cx="16" cy="16" r="16" fill="#fff"/><path d="M16 10a5 5 0 0 0-3 9v2h6v-2a5 5 0 0 0-3-9z" fill="none" stroke="#111" stroke-width="1.6"/><path d="M13.5 23h5M16 5v2M9 8l1.4 1.4M23 8l-1.4 1.4M7 15h2M23 15h2" stroke="#111" stroke-width="1.3"/></svg>
      We make sure you get<br>the BEST deal possible
    </div>
    <div class="benefit" style="left:9px;top:173px">
      <svg width="32" height="32" viewBox="0 0 32 32"><circle cx="16" cy="16" r="16" fill="#fff"/><circle cx="12" cy="11" r="2" fill="#111"/><circle cx="20" cy="11" r="2" fill="#111"/><path d="M10 14h4v6h-1v5h-2v-5h-1zM18 14h4v6h-1v5h-2v-5h-1z" fill="#111"/></svg>
      We help you enroll
    </div>
    <div class="benefit" style="left:116px;top:173px">
      <svg width="32" height="32" viewBox="0 0 32 32"><circle cx="16" cy="16" r="16" fill="#fff"/><circle cx="16" cy="16" r="8" fill="none" stroke="#111" stroke-width="1.8"/><path d="M20 12l-2.5 5.5L12 20l2.5-5.5z" fill="#111"/></svg>
      We navigate you<br>through health reform
    </div>
    <div class="benefit" style="left:219px;top:173px">
      <svg width="32" height="32" viewBox="0 0 32 32"><circle cx="16" cy="16" r="16" fill="#fff"/><path d="M8 16a8 7 0 0 1 16 0z" fill="#111"/><path d="M16 16v6a2 2 0 0 1-4 0" fill="none" stroke="#111" stroke-width="1.5"/></svg>
      We're always here
    </div>

    <div class="quote-button">GET YOUR QUOTE NOW</div>
  </section>
  <svg class="notch-top" width="14" height="9" viewBox="0 0 14 9"><path d="M0 0h14L7 9z" fill="#fff"/></svg>
  <svg class="notch-bottom" width="14" height="9" viewBox="0 0 14 9"><path d="M0 0h14L7 9z" fill="#88c2dc"/></svg>

  <section class="carriers">
    <h2>Choices for affordable health coverage :</h2>
    <ul class="carrier-row">
      <li class="carrier">Aldena</li>
      <li class="carrier">Northfield One</li>
      <li class="carrier">Bayline Mutual</li>
      <li class="carrier">Cresta</li>
      <li class="carrier">Verdan</li>
    </ul>
    <div class="dots" style="left:142px;top:43px"><span class="on"></span><span></span><span></span></div>
  </section>

  <section class="testimonial">
    <div class="avatar" role="img" aria-label="A smiling mother hugging her young daughter"></div>
    <blockquote>I want to thank you so much for <em>making time to chat with me and help me figure out my health insurance.</em> You definitely saved me from a complete meltdown or two! I would highly recommend you to anyone that asked.</blockquote>
    <div class="dots"><span class="on"></span><span></span><span></span></div>
  </section>

  <footer class="site-footer">
    <div class="social"><span></span><span></span><span></span><span></span><span></span></div>
    <div class="footer-col" style="left:16px">
      <h3>Programs &amp; Partners</h3>
      <ul><li>Certified Insurance Agents</li><li>Regional Labor Plans</li><li>Enrollment Assistance</li><li>Program</li><li>Health Insurance Companies</li><li>Outreach &amp; Education</li><li>Small Business Health Plans</li><li>Companies</li></ul>
    </div>
    <div class="footer-col" style="left:89px">
      <h3>The Board</h3>
      <ul><li>Board Members</li><li>Board Meetings</li></ul>
    </div>
    <div class="footer-col" style="left:177px">
      <h3>Connect with Us</h3>
      <ul><li>Contact Us</li><li>Careers Openings</li><li>Request for a Hearing</li><li>Report an Eligibility</li><li>Determination</li><li>Inbound Call Center</li><li>Public Records Request</li><li>&nbsp;</li><li>Health Benefit Exchange</li><li>Job Opportunities</li></ul>
    </div>
    <div class="footer-col" style="left:257px">
      <h3>Resources</h3>
      <ul><li>Reference Guide</li><li>Privacy Policy</li><li>Verify a Certified</li><li>Agent</li><li>Regulations</li><li>Federal Guidance</li><li>Notice of Practices</li><li>Program Toolkit</li><li>Get Help</li><li>Fact Sheets</li><li>Register to Vote</li></ul>
    </div>
    <p class="footer-note">Pacific Shield Exchange is a joint partnership of Pacific Shield and the Harbor State Health Office.</p>
  </footer>

</div>
</body>
</html>
```